Financial Services Consultant needs a business card

We need a business card for a new consulting company based in Melbourne called
"Korvane Metrics". Tagline is Measure, Monitor, Save
We would like to see business card designs that are in line with the minimal style of the website www.korvane-metrics-example.com
The font I have used on the website is Proxima Nova and would like the same or similar font used on the business card with a minimal design in line with the website Two sided with "KORVANE METRICS" MEASURE, MONITOR, SAVE on one side and name, title and contact details on the otther
Updates

Hi All, thanks for your submissions, much appreciated.

I have recently added some colour to my webiste, it is hex #3a7b74 for those that wish to use it
Thanks

Hi all

thanks very much for your design submissions I am very impressed and they are much appreciated.

Interms of general feedback please find below;

Colour: I am trying to stick to a minimal design and colour scheme for my website which is still under construction, up to 3 colours( www.korvane-metrics-example.com) it is currently black and white with a small amount of blue/green but I am open to suggestion/interpretations for a consulting company.

Card: I dont mind if it has rounded edges or straight, I was thinking about using a letterpress card if possible

Detail: the detail on the card will include; Name, Title, Mobile, Personal Email, Business Email,Web,Business Address

Once again thanks for submissions

Industry/Entity Type

Business

```html
<!DOCTYPE html>
<html lang="en">
<head>
<meta charset="utf-8">
<title>Korvane Metrics – Business Card</title>
<link href="https://fonts.googleapis.com/css2?family=Open+Sans:wght@400;600;700&display=swap" rel="stylesheet">
<style>
  :root {
    --brand-green: #2f936a;
    --ink: #1c1c1c;
    --paper: #ffffff;
    --backdrop: #e6e6e4;
    --rule: #3a3a3a;
  }
  * { margin: 0; padding: 0; box-sizing: border-box; }
  html, body {
    width: 1200px; height: 856px; overflow: hidden;
    background: var(--backdrop);
    font-family: "Open Sans", sans-serif;
  }
  .stage {
    position: relative; width: 1200px; height: 856px;
    display: flex; align-items: center; justify-content: center; gap: 50px;
  }
  .card {
    position: relative; width: 525px; height: 300px;
    background: var(--paper);
    box-shadow: 0 2px 10px rgba(0,0,0,0.12);
    overflow: hidden;
  }
  /* Front */
  .front__name {
    position: absolute; left: 52px; top: 100px;
    font-weight: 700; font-size: 44px; letter-spacing: 2px;
    color: var(--brand-green); white-space: nowrap;
  }
  .front__tagline {
    position: absolute; left: 60px; top: 166px;
    font-size: 13px; letter-spacing: 1px; color: var(--ink);
    text-transform: uppercase;
  }
  /* Back */
  .back__rule { position: absolute; height: 1px; background: var(--rule); }
  .back__rule--top { left: 34px; right: 0; top: 40px; }
  .back__rule--bottom { left: 34px; right: 34px; top: 170px; }
  .back__tagline {
    position: absolute; right: 34px; top: 58px;
    font-weight: 700; font-size: 18px; letter-spacing: 2px;
    color: var(--brand-green); white-space: nowrap;
  }
  .back__person { position: absolute; left: 34px; top: 104px; }
  .back__name {
    font-weight: 700; font-size: 20px; letter-spacing: 1px;
    color: var(--brand-green);
  }
  .back__title { font-size: 17px; color: var(--ink); margin-top: 2px; }
  .back__contact {
    position: absolute; right: 34px; top: 196px;
    display: flex; align-items: stretch; gap: 8px;
  }
  .contact__lines {
    text-align: right; font-size: 15px; line-height: 25px;
    letter-spacing: 0.5px; color: var(--ink); white-space: nowrap;
  }
  .contact__icons {
    border-left: 1px solid var(--rule); padding-left: 6px;
    display: flex; flex-direction: column; justify-content: space-around;
  }
  .contact__icons svg { width: 13px; height: 13px; display: block; }
</style>
</head>
<body>
<main class="stage">
  <section class="card card--front" aria-label="Card front">
    <h1 class="front__name">KORVANE METRICS</h1>
    <p class="front__tagline">Assess, Track, Retain</p>
  </section>

  <section class="card card--back" aria-label="Card back">
    <div class="back__rule back__rule--top"></div>
    <p class="back__tagline">ASSESS, TRACK, RETAIN</p>
    <div class="back__person">
      <h2 class="back__name">Daniel Hartwell</h2>
      <p class="back__title">Director</p>
    </div>
    <div class="back__rule back__rule--bottom"></div>
    <div class="back__contact">
      <div class="contact__lines">
        <p>04 1234 5670</p>
        <p>korvane.metrics@example.com</p>
        <p>www.korvane-metrics-example.com</p>
      </div>
      <div class="contact__icons">
        <svg viewBox="0 0 14 14" aria-label="Phone"><rect x="4" y="1" width="6" height="12" rx="1" fill="none" stroke="#2f936a" stroke-width="1.2"/><line x1="6" y1="11" x2="8" y2="11" stroke="#2f936a"/></svg>
        <svg viewBox="0 0 14 14" aria-label="Email"><rect x="1" y="3" width="12" height="8" fill="none" stroke="#2f936a" stroke-width="1.2"/><polyline points="1,3 7,8 13,3" fill="none" stroke="#2f936a" stroke-width="1.2"/></svg>
        <svg viewBox="0 0 14 14" aria-label="Website"><circle cx="7" cy="7" r="5.5" fill="none" stroke="#2f936a" stroke-width="1.2"/><ellipse cx="7" cy="7" rx="2.5" ry="5.5" fill="none" stroke="#2f936a"/><line x1="1.5" y1="7" x2="12.5" y2="7" stroke="#2f936a"/></svg>
      </div>
    </div>
  </section>
</main>
</body>
</html>
```